Business Card for a Dental Office

The design should communicate integrity, quality and reliability. We also want the card look elegant, simple, but still stand out, different from the traditional-dental-office business card.

Industry/Entity Type

Business

```html
<!DOCTYPE html>
<html lang="en">
<head>
<meta charset="utf-8">
<title>Harbor Dental Studio – Business Card</title>
<link rel="stylesheet" href="https://fonts.googleapis.com/css2?family=Oswald:wght@500&family=Open+Sans:wght@400;600&display=swap">
<style>
  :root {
    --backdrop: #4b4b4b;
    --card-white: #ffffff;
    --ink: #111111;
    --ink-soft: #444444;
    --rule: #cfcfcf;
    --gold: #c9a521;
    --gold-bright: #f2e01c;
    --gold-deep: #a8861a;
    --black: #000000;
  }
  * { margin: 0; padding: 0; box-sizing: border-box; }
  html, body {
    width: 1105px; height: 1200px; overflow: hidden;
    background: var(--backdrop);
    font-family: "Open Sans", Arial, sans-serif;
  }
  .stage { position: relative; width: 1105px; height: 1200px; }
  .card { position: absolute; left: 196px; width: 720px; height: 412px; overflow: hidden; }
  .card--front { top: 146px; background: var(--card-white); }
  .card--back { top: 602px; background: var(--black); }

  /* Front */
  .brand {
    position: absolute; left: 180px; top: 100px;
    display: flex; align-items: center; gap: 14px; white-space: nowrap;
  }
  .brand__mark { width: 62px; height: 62px; background: var(--ink); flex: none; }
  .brand__name {
    font-family: "Oswald", Arial, sans-serif; font-weight: 500;
    font-size: 32px; line-height: 34px; color: var(--ink); letter-spacing: 0.4px;
  }
  .brand__tagline {
    font-family: "Oswald", Arial, sans-serif; font-weight: 500;
    font-size: 15px; line-height: 18px; color: var(--gold); letter-spacing: 2.1px;
    text-transform: uppercase;
  }
  .person {
    position: absolute; right: 387px; top: 212px; text-align: right; white-space: nowrap;
    font-size: 17.5px; line-height: 27.6px; color: var(--ink-soft);
  }
  .person__name { font-size: 24px; font-weight: 600; color: var(--ink); }
  .person__role { color: var(--gold); }
  .divider { position: absolute; left: 356px; top: 212px; width: 1px; height: 118px; background: var(--rule); }
  .contacts {
    position: absolute; left: 385px; top: 212px; list-style: none; white-space: nowrap;
    font-size: 17.5px; line-height: 27.6px; color: var(--ink-soft);
  }
  .contacts li { display: flex; align-items: center; gap: 9px; }
  .contacts svg { width: 17px; height: 17px; fill: var(--ink); flex: none; }
  .band-line { position: absolute; left: 0; top: 374px; width: 100%; height: 4px; background: var(--gold); }
  .band { position: absolute; left: 0; top: 384px; width: 100%; height: 28px; background: var(--black); }

  /* Back */
  .emblem {
    position: absolute; left: 60px; top: 40px; width: 320px; height: 320px;
    background: linear-gradient(135deg, var(--gold-deep), var(--gold-bright) 55%, var(--gold));
  }
  .back-brand { position: absolute; left: 407px; top: 300px; color: var(--gold-bright); white-space: nowrap; }
  .back-brand__name {
    font-family: "Oswald", Arial, sans-serif; font-weight: 500;
    font-size: 28px; line-height: 30px; letter-spacing: 0.3px;
  }
  .back-brand__tagline {
    font-family: "Oswald", Arial, sans-serif; font-weight: 500;
    font-size: 12.5px; line-height: 15px; letter-spacing: 1px; text-transform: uppercase; margin-top: 1px;
  }
  .back-brand__web { font-size: 16px; line-height: 20px; letter-spacing: 4.2px; margin-top: 5px; color: var(--gold); }
</style>
</head>
<body>
<main class="stage">
  <section class="card card--front" aria-label="Card front">
    <div class="brand">
      <div class="brand__mark"></div>
      <div>
        <div class="brand__name">HARBOR DENTAL STUDIO</div>
        <div class="brand__tagline">Your smile is your gift to others</div>
      </div>
    </div>

    <div class="person">
      <div class="person__name">Daniel Reeves</div>
      <div class="person__role">CEO/Founder</div>
      <div>142 Willow Creek Road</div>
      <div>Fairview, Oregon 97024</div>
    </div>

    <div class="divider"></div>

    <ul class="contacts">
      <li><svg viewBox="0 0 24 24"><path d="M6.6 10.8a15 15 0 0 0 6.6 6.6l2.2-2.2a1 1 0 0 1 1-.25 11.4 11.4 0 0 0 3.6.57 1 1 0 0 1 1 1V20a1 1 0 0 1-1 1A17 17 0 0 1 3 4a1 1 0 0 1 1-1h3.5a1 1 0 0 1 1 1c0 1.25.2 2.45.57 3.57a1 1 0 0 1-.25 1z"/></svg>555 210 4837</li>
      <li><svg viewBox="0 0 24 24"><path d="M7 1h10a2 2 0 0 1 2 2v18a2 2 0 0 1-2 2H7a2 2 0 0 1-2-2V3a2 2 0 0 1 2-2zm0 3v14h10V4zm5 15.5a1.2 1.2 0 1 0 0 2.4 1.2 1.2 0 0 0 0-2.4z"/></svg>555 318 7720</li>
      <li><svg viewBox="0 0 24 24"><path d="M2 5h20v14H2zm2 2v.4l8 5.2 8-5.2V7zm0 2.8V17h16V9.8l-8 5.2z"/></svg>hello@harbordental.com</li>
      <li><svg viewBox="0 0 24 24"><path d="M12 2a10 10 0 1 0 0 20 10 10 0 0 0 0-20zm-1 17.9A8 8 0 0 1 4.1 11H7l2 2v2l2 2zm6.9-2.6A2 2 0 0 0 16 16h-1v-3a1 1 0 0 0-1-1H8v-2h2a1 1 0 0 0 1-1V7h2a2 2 0 0 0 2-2v-.4a8 8 0 0 1 2.9 12.7z"/></svg>www.harbordental.com</li>
    </ul>

    <div class="band-line"></div>
    <div class="band"></div>
  </section>

  <section class="card card--back" aria-label="Card back">
    <div class="emblem" aria-hidden="true"></div>
    <div class="back-brand">
      <div class="back-brand__name">HARBOR DENTAL STUDIO</div>
      <div class="back-brand__tagline">Your smile is your gift to others</div>
      <div class="back-brand__web">www.harbordental.com</div>
    </div>
  </section>
</main>
</body>
</html>
```